Design a modern, classy & professional business card for an online real estate agency, specializing in medium-luxury properties in Thailand and later in Singapore and UK.

Possible design ideas so far: (not essential)

- curved corner(s) to the card, white on front & turquoise on back or visa versa.

- front of card - clear and simple, company name in metallic grey/monochrome, logo graphic & company name on front in spot UV or embossed/debossed effect.

- back of card - large, close-cropped, 'ghost' patterns of the C-shaped curves of logo, or company name repeated on back of card in spot UV.

Target Market(s)

- young to middle-aged professionals mainly (but ideally should design should suit all)

- UK, US,EU,AUS & ASIAN mainly (but ideally should design should suit all countries)

Industry/Entity Type

Real Estate

Requirements
Must have
• THEME:
- Luxurious & Modern
- Clean & striking
- Unique & creative

INFO:
- Logo & company name on front
- Contact details on back:

Tobias Lindqvar
Managing Director

www.velmoraestates.example
www.velmoraestates-uk.example

Tel: 084-273-6190
email: tobias@velmoraestates.example

(contact details can be displayed in any order as suites design.)

Nice to have
• - curved corner(s) to the card, white on front & turquoise on back or visa versa.

Should not have
• - No generic images of properties, palm trees/coconut trees etc.

- No other other bold colors, except for main turquoise, grey, metallic white & black theme.

- No obvious business card templates

```html
<!DOCTYPE html>
<html lang="en">
<head>
<meta charset="utf-8">
<title>Velmora Estates – Business Card</title>
<link href="https://fonts.googleapis.com/css2?family=Exo+2:wght@400;600;700&display=swap" rel="stylesheet">
<style>
  :root {
    --page-bg: #ece8e1;
    --front-bg: #8fd0e6;
    --front-ink: #1c2530;
    --back-bg: #252a25;
    --back-accent: #3ec3b2;
    --back-muted: #6fb8ae;
    --back-ghost: #2e342f;
    --card-radius: 38px;
  }
  * { margin: 0; padding: 0; box-sizing: border-box; }
  html, body {
    width: 1200px;
    height: 1000px;
    overflow: hidden;
    background: var(--page-bg);
    font-family: "Exo 2", sans-serif;
  }
  .canvas {
    position: relative;
    width: 1200px;
    height: 1000px;
  }
  .card {
    position: absolute;
    left: 300px;
    width: 600px;
    height: 340px;
    border-radius: var(--card-radius);
    overflow: hidden;
    box-shadow: 0 10px 30px rgba(0, 0, 0, 0.12);
  }

  /* Front */
  .card-front {
    top: 120px;
    background: var(--front-bg);
    display: flex;
    align-items: center;
    padding-left: 58px;
    gap: 22px;
  }
  .brand-square {
    width: 104px;
    height: 104px;
    background: var(--front-ink);
    flex-shrink: 0;
  }
  .brand-name {
    color: var(--front-ink);
    font-weight: 600;
    font-size: 50px;
    letter-spacing: 0.5px;
    white-space: nowrap;
  }

  /* Back */
  .card-back {
    top: 540px;
    background: var(--back-bg);
    padding: 44px 46px;
  }
  .person-name {
    color: var(--back-accent);
    font-weight: 700;
    font-size: 26px;
    letter-spacing: 0.5px;
  }
  .person-title {
    color: var(--back-muted);
    font-size: 13px;
    margin-top: 8px;
  }
  .contact-list {
    position: absolute;
    left: 46px;
    bottom: 40px;
    list-style: none;
    color: var(--back-accent);
    font-size: 14px;
    line-height: 1.45;
  }
  .contact-list .gap { margin-top: 12px; }
  .ghost-name {
    position: absolute;
    right: 36px;
    top: 120px;
    color: var(--back-ghost);
    font-weight: 600;
    font-size: 40px;
    white-space: nowrap;
  }
</style>
</head>
<body>
  <main class="canvas">
    <section class="card card-front" aria-label="Card front">
      <div class="brand-square"></div>
      <div class="brand-name">Velmora Estates</div>
    </section>

    <section class="card card-back" aria-label="Card back">
      <h1 class="person-name">Tobias Lindqvar</h1>
      <p class="person-title">Managing Director</p>
      <div class="ghost-name">Velmora Estates</div>
      <ul class="contact-list">
        <li>www.velmoraestates.example</li>
        <li>www.velmoraestates-uk.example</li>
        <li class="gap">Tel: 084-273-6190</li>
        <li>email: tobias@velmoraestates.example</li>
      </ul>
    </section>
  </main>
</body>
</html>
```